Self Defence Seminar Flyer

Need a flyer that will sell a seminar that will teach self defence techniques to customers. Needs to have a good image that will remind people about the dangerous world. The seminar is for men and women.

Needs to look professional.

I have attached the previous flyer we used. needs same information except without the same date and time for seminar.

Target Market(s)

Male and Females interested in learning how to defend themselves or family

Industry/Entity Type

Defence

Requirements
Must have
• A Image that reminds people of a dangerous situation

```html
<!DOCTYPE html>
<html lang="en">
<head>
<meta charset="utf-8">
<title>Self Defence Seminar</title>
<link rel="stylesheet" href="https://fonts.googleapis.com/css2?family=Russo+One&family=Exo+2:wght@300;500&family=Audiowide&display=swap">
<style>
  :root {
    --bg: #050303;
    --figure-red: #7c1a14;
    --figure-mid: #561009;
    --figure-deep: #240604;
    --title-white: #ffffff;
    --title-orange: #e2650f;
    --body-white: #f4f4f4;
    --info-cyan: #2fe0e6;
    --cta-orange: #f07a12;
    --frame-red: #d8161b;
    --logo-light: #f2f2f2;
  }
  * { margin: 0; padding: 0; box-sizing: border-box; }
  html, body { width: 850px; height: 1200px; overflow: hidden; background: var(--bg); }
  .flyer {
    position: relative;
    width: 850px;
    height: 1200px;
    overflow: hidden;
    background: linear-gradient(160deg, #120606 0%, var(--bg) 55%, #0b0706 100%);
  }
  .hero-figure {
    position: absolute;
    left: 0;
    top: 70px;
    width: 560px;
    height: 1130px;
    background:
      radial-gradient(ellipse 60% 48% at 38% 42%, var(--figure-red) 0%, var(--figure-mid) 45%, var(--figure-deep) 78%, transparent 100%);
  }
  .title {
    position: absolute;
    left: 0;
    right: 0;
    top: 20px;
    text-align: center;
    font-family: "Russo One", sans-serif;
    color: var(--title-white);
    -webkit-text-stroke: 3px #000;
    paint-order: stroke fill;
    line-height: 1;
  }
  .title-band {
    position: absolute;
    left: 132px;
    top: 72px;
    width: 560px;
    height: 34px;
    background: var(--title-orange);
    border-radius: 6px;
  }
  .title-top { position: relative; display: block; font-size: 78px; letter-spacing: 1px; }
  .title-main { position: relative; display: block; font-size: 112px; letter-spacing: 2px; margin-top: 0; }
  .selling-points {
    position: absolute;
    left: 259px;
    top: 220px;
    width: 585px;
    list-style: none;
    font-family: "Exo 2", sans-serif;
    font-weight: 500;
    font-size: 18.5px;
    line-height: 25px;
    color: var(--body-white);
    white-space: nowrap;
  }
  .selling-points li {
    position: relative;
    padding-left: 85px;
    text-indent: -25px;
    margin-bottom: 26px;
  }
  .selling-points li::before {
    content: "•";
    position: absolute;
    left: -25px;
    text-indent: 0;
  }
  .seminar-info {
    position: absolute;
    left: 0;
    right: 0;
    top: 710px;
    text-align: center;
    font-family: "Audiowide", sans-serif;
    font-size: 30px;
    line-height: 42px;
    color: var(--info-cyan);
  }
  .call-to-action {
    position: absolute;
    left: 0;
    right: 0;
    top: 846px;
    text-align: center;
    font-family: "Exo 2", sans-serif;
    font-weight: 300;
    font-size: 28px;
    line-height: 40px;
    color: var(--cta-orange);
  }
  .host-badge {
    position: absolute;
    left: 22px;
    top: 972px;
    width: 297px;
    height: 209px;
    background: var(--logo-light);
    display: flex;
    align-items: center;
    justify-content: center;
    font-family: "Russo One", sans-serif;
    font-size: 28px;
    color: var(--title-orange);
  }
  .partner-badge {
    position: absolute;
    left: 469px;
    top: 975px;
    width: 362px;
    height: 206px;
    background: #0b0b0b;
    border: 3px solid var(--frame-red);
    display: flex;
    align-items: center;
    justify-content: center;
    font-family: "Russo One", sans-serif;
    font-size: 30px;
    color: var(--logo-light);
  }
</style>
</head>
<body>
  <main class="flyer">
    <div class="hero-figure" role="img" aria-label="Illustration area: menacing dark red figure in shadow, suggesting danger"></div>

    <header class="title">
      <div class="title-band"></div>
      <h1>
        <span class="title-top">SELF DEFENCE</span>
        <span class="title-main">SEMINAR</span>
      </h1>
    </header>

    <ul class="selling-points">
      <li>Being a victim is a topic that people would like to avoid.<br>Unfortunately, we live in an increasingly dangerous<br>society for men and women alike. Learning to<br>defend yourself is an important life skill</li>
      <li>Spend 2 Hours with us learning some simple and<br>effective Self Defence tactics that one-day may be<br>needed to defend yourself or loved ones.</li>
      <li>Our aim is to teach you effective and efficient<br>techniques and tactics to be able to defend yourself<br>in a range of situations.</li>
      <li>Learn the same techniques and tactics that we have<br>taught to individuals in Law enforcement, Security,<br>and Military.</li>
      <li>We incoporeated weapon defence, use of surroundings<br>and psycological techniques in our classes.</li>
    </ul>

    <section class="seminar-info">
      <p>Cost - $60.00</p>
      <p>Location - Iron Harbour Combat Gym</p>
      <p>(214 Westbrook Rd. Greyfield NSW)</p>
    </section>

    <section class="call-to-action">
      <p>Sign up today by contacting us though our website</p>
      <p>www.ironharbourcombat.com</p>
    </section>

    <div class="host-badge">Team Iron Harbour</div>
    <div class="partner-badge">Northgate Fight Club</div>
  </main>
</body>
</html>
```